Advertising material for new program

We are launching a new program and need some advertising material.
- Cover photo for facebook (with minimal words on it)
- Social Media graphic (with minimal words on it)
- a5 flyer
- Banner

Information:
- Sensory play is a NEW program at Ember Tumblehall
What is Sensory Play:
*A sensory experience for babies 0 - 13months old.
* Stimulating babies senses
* Engaging movement and balance
- Created by qualified early childhood professional
- starting on Wednesdays in February 2022
- Book online
*www.embertumblehall.example
-Contact us for more information
*97316258
*info@embertumblehall.example

NOT INFORMATION FOR THE ADVERTISING
I have attached our style guide, our logo, some material we have done done recently and some photo of my own baby. As its a new program we don't have any photos yet but I am open to ideas

Target Market(s)

Mums aged 25 - 45

Industry/Entity Type

Kids activities

Colors
0054AA
0677BA
7BADD7
CADEEF
E8F1F8
59FF00
82FF00
B8FF75
E3FFCB
F4FFEA

Requirements
Must have
• photos of babies and mums with babies
Should not have
• Photos of adults / teens

```html
<!DOCTYPE html>
<html lang="en">
<head>
<meta charset="utf-8">
<title>Sensory Play – Ember Tumblehall</title>
<link rel="stylesheet" href="https://fonts.googleapis.com/css2?family=Anton&family=Graduate&family=Montserrat:ital,wght@0,800;1,900&family=Open+Sans:wght@700;800&family=Oswald:wght@600&display=swap">
<style>
  :root {
    --navy: #0b2147;
    --lime: #9bc90a;
    --lime-bright: #b4e01a;
    --white: #ffffff;
    --grey-deep: #4f4f56;
    --grey-dark: #77777e;
    --grey-mid: #a4a4aa;
    --grey-soft: #cfcfd4;
    --grey-light: #ececef;
  }
  * { margin: 0; padding: 0; box-sizing: border-box; }
  html, body { width: 1200px; height: 675px; overflow: hidden; background: var(--white); }
  .flyer {
    position: relative;
    width: 1200px;
    height: 675px;
    overflow: hidden;
    background: var(--white);
    font-family: "Open Sans", sans-serif;
    color: var(--navy);
  }
  .photo-area {
    position: absolute;
    left: 0; top: 0;
    width: 820px; height: 675px;
    background:
      radial-gradient(ellipse 420px 230px at 380px 700px, var(--grey-deep), transparent 72%),
      radial-gradient(ellipse 300px 180px at 560px 560px, var(--grey-dark), transparent 70%),
      radial-gradient(ellipse 170px 190px at 440px 200px, #f4f4f6, transparent 70%),
      radial-gradient(ellipse 200px 140px at 470px 390px, #e2e2e6, transparent 70%),
      radial-gradient(ellipse 110px 260px at 20px 300px, var(--grey-mid), transparent 72%),
      radial-gradient(ellipse 140px 110px at 330px 120px, var(--grey-soft), transparent 70%),
      linear-gradient(180deg, var(--grey-light) 0%, var(--grey-soft) 55%, var(--grey-mid) 100%);
    -webkit-mask-image: linear-gradient(90deg, #000 74%, transparent 94%);
    mask-image: linear-gradient(90deg, #000 74%, transparent 94%);
  }
  .accent-wash {
    position: absolute;
    inset: 0;
    background:
      radial-gradient(ellipse 150px 70px at 1180px 20px, rgba(155,201,10,.5), transparent 70%),
      radial-gradient(ellipse 170px 70px at 760px 640px, rgba(155,201,10,.5), transparent 70%),
      radial-gradient(ellipse 90px 150px at 1195px 560px, rgba(155,201,10,.45), transparent 70%),
      radial-gradient(ellipse 110px 50px at 690px 40px, rgba(155,201,10,.4), transparent 70%),
      radial-gradient(ellipse 50px 120px at 650px 150px, rgba(155,201,10,.25), transparent 70%);
    pointer-events: none;
  }
  .brand {
    position: absolute;
    left: 72px; top: 80px;
    display: flex; align-items: center; gap: 14px;
    font-family: "Open Sans", sans-serif;
    font-weight: 800;
    font-size: 40px;
    color: var(--navy);
  }
  .brand-dot { width: 30px; height: 30px; border-radius: 50%; background: var(--lime); }

  .start-label {
    position: absolute;
    left: 56px; top: 316px;
    font-family: "Open Sans", sans-serif;
    font-weight: 800;
    font-size: 27px;
    color: var(--navy);
    -webkit-text-stroke: 4px var(--white);
    paint-order: stroke fill;
  }
  .day-bar {
    position: absolute;
    left: 57px; top: 358px;
    width: 280px; height: 40px;
    background: var(--lime);
    border-right: 10px solid var(--navy);
    padding-left: 14px;
    font-family: "Montserrat", sans-serif;
    font-weight: 800;
    font-size: 33px;
    line-height: 40px;
    color: var(--white);
    letter-spacing: .5px;
  }
  .date-art {
    position: absolute;
    left: 50px; top: 408px;
    width: 310px; height: 180px;
    overflow: visible;
    font-family: "Graduate", serif;
  }
  .date-outer { fill: var(--white); stroke: var(--white); stroke-linejoin: round; }
  .date-inner { fill: var(--lime); stroke: var(--navy); stroke-linejoin: round; paint-order: stroke fill; }

  .booking {
    position: absolute;
    left: 830px; top: 46px;
    width: 260px;
    text-align: center;
    font-weight: 700;
  }
  .booking-title { font-size: 16px; letter-spacing: .5px; }
  .booking-link {
    margin-top: 8px;
    display: flex; align-items: center; justify-content: center; gap: 10px;
    font-size: 13px;
  }
  .icon { width: 30px; height: 30px; flex: none; }

  .program-title {
    position: absolute;
    left: 735px; top: 128px;
    width: 445px;
    text-align: center;
    font-family: "Anton", sans-serif;
    font-size: 66px;
    line-height: 76px;
    letter-spacing: 1px;
    color: var(--navy);
    transform: skewX(-8deg);
    -webkit-text-stroke: 8px var(--lime-bright);
    paint-order: stroke fill;
    text-shadow: 2px 4px 6px rgba(0,0,0,.25);
  }
  .program-tag {
    position: absolute;
    left: 800px; top: 214px;
    width: 310px;
    text-align: center;
    font-family: "Montserrat", sans-serif;
    font-style: italic;
    font-weight: 900;
    font-size: 21px;
    color: var(--lime);
    -webkit-text-stroke: 1.5px var(--navy);
    paint-order: stroke fill;
  }
  .age-band {
    position: absolute;
    left: 762px; top: 257px;
    width: 386px; height: 34px;
    background: var(--navy);
    transform: skewX(-14deg);
    border-bottom: 3px solid var(--lime);
    box-shadow: 3px 4px 6px rgba(0,0,0,.2);
  }
  .age-text {
    position: absolute;
    left: 762px; top: 257px;
    width: 386px; height: 34px;
    text-align: center;
    line-height: 34px;
    font-weight: 800;
    font-size: 21px;
    color: var(--white);
  }
  .credit {
    position: absolute;
    left: 760px; top: 306px;
    width: 390px;
    text-align: center;
    font-family: "Montserrat", sans-serif;
    font-weight: 800;
    font-size: 25px;
    line-height: 30px;
    color: var(--navy);
    -webkit-text-stroke: 5px var(--lime-bright);
    paint-order: stroke fill;
  }
  .benefits {
    position: absolute;
    left: 775px; top: 415px;
    width: 370px;
    list-style: none;
    text-align: center;
    font-weight: 700;
    font-size: 17px;
    line-height: 30px;
  }
  .benefits li::before { content: "* "; }

  .call-box {
    position: absolute;
    left: 825px; top: 490px;
    width: 295px; height: 75px;
  }
  .call-shape { position: absolute; inset: 0; width: 100%; height: 100%; }
  .call-content {
    position: absolute;
    left: 72px; top: 14px;
    display: flex; align-items: center; gap: 8px;
  }
  .call-text { font-family: "Oswald", sans-serif; font-weight: 600; line-height: 1; }
  .call-label { font-size: 13px; color: var(--white); }
  .call-number { font-size: 20px; color: var(--lime-bright); margin-top: 3px; letter-spacing: .5px; }

  .email {
    position: absolute;
    left: 860px; top: 578px;
    display: flex; align-items: center; gap: 8px;
    font-weight: 700;
    font-size: 13px;
  }
</style>
</head>
<body>
<main class="flyer">
  <div class="photo-area" role="img" aria-label="Black and white photo of a smiling mum holding her baby on an exercise ball while the baby chews a rattle"></div>
  <div class="accent-wash" aria-hidden="true"></div>

  <div class="brand"><span class="brand-dot"></span>Ember Tumblehall</div>

  <p class="start-label">STARTING ON</p>
  <p class="day-bar">WEDNESDAYS</p>

  <svg class="date-art" viewBox="0 0 310 180" role="img" aria-label="February 2022">
    <text class="date-outer" x="10" y="58" font-size="60" stroke-width="11" textLength="283" lengthAdjust="spacingAndGlyphs">FEBRUARY</text>
    <text class="date-inner" x="10" y="58" font-size="60" stroke-width="5" textLength="283" lengthAdjust="spacingAndGlyphs">FEBRUARY</text>
    <text class="date-outer" x="8" y="165" font-size="126" stroke-width="18" textLength="287" lengthAdjust="spacingAndGlyphs">2022</text>
    <text class="date-inner" x="8" y="165" font-size="126" stroke-width="10" textLength="287" lengthAdjust="spacingAndGlyphs">2022</text>
  </svg>

  <section class="booking">
    <p class="booking-title">BOOK ONLINE</p>
    <p class="booking-link">
      <svg class="icon" viewBox="0 0 30 30" aria-hidden="true">
        <g fill="none" stroke="var(--navy)" stroke-width="2.4">
          <circle cx="15" cy="15" r="12"/>
          <ellipse cx="15" cy="15" rx="5.5" ry="12"/>
          <line x1="3" y1="15" x2="27" y2="15"/>
          <line x1="5" y1="9" x2="25" y2="9"/>
          <line x1="5" y1="21" x2="25" y2="21"/>
        </g>
      </svg>
      WWW.EMBERTUMBLEHALL.EXAMPLE
    </p>
  </section>

  <h1 class="program-title">SENSORY PLAY</h1>
  <p class="program-tag">NEW PROGRAM</p>

  <div class="age-band" aria-hidden="true"></div>
  <p class="age-text">FOR BABIES 0 - 13 MONTHS OLD</p>

  <p class="credit">CREATES BY<br>QUALIFIED EARLY<br>CHILDHOOD PROFESSIONAL</p>

  <ul class="benefits">
    <li>STIMULATING BABIES SENSES</li>
    <li>ENGAGING MOVEMENT AND BALANCE</li>
  </ul>

  <div class="call-box">
    <svg class="call-shape" viewBox="0 0 295 75" preserveAspectRatio="none" aria-hidden="true">
      <path fill="var(--navy)" d="M4 18 L40 10 L120 6 L210 4 L280 10 L290 20 L286 34 L294 46 L284 58 L240 64 L170 70 L90 72 L30 66 L10 58 L14 44 L2 32 Z"/>
    </svg>
    <div class="call-content">
      <svg class="icon" viewBox="0 0 30 30" aria-hidden="true">
        <rect x="6" y="3" width="13" height="24" rx="2.5" fill="none" stroke="var(--white)" stroke-width="2.2"/>
        <circle cx="12.5" cy="22.5" r="1.6" fill="var(--white)"/>
        <path d="M22 11 q3 4 0 8 M25 9 q4 6 0 12" fill="none" stroke="var(--white)" stroke-width="1.6"/>
      </svg>
      <div class="call-text">
        <p class="call-label">Call Now</p>
        <p class="call-number">02 97316258</p>
      </div>
    </div>
  </div>

  <p class="email">
    <svg class="icon" viewBox="0 0 30 30" aria-hidden="true">
      <g fill="none" stroke="var(--navy)" stroke-width="2.2" stroke-linejoin="round">
        <path d="M3 13 L15 4 L27 13 V27 H3 Z"/>
        <path d="M3 13 L15 21 L27 13"/>
        <path d="M3 27 L12 19 M27 27 L18 19"/>
      </g>
    </svg>
    INFO@EMBERTUMBLEHALL.EXAMPLE
  </p>
</main>
</body>
</html>
```